Dawson's Lawn Service needs a postcard design

I need a design to attract lawn cutting customers. I am a high school junior, focusing on my city and the neighboring city. I think it would be advantageous to let my potential clients know I am earning money for my college education. They should also know, I will be working side by side with my father, who operated his own lawn service for 20 years, so they can be assured of a quality result for their lawn. I will be using state of the art, commercial equipment.

A few things that are unique to my service are; my mower weighs half of what other commercial mowers do (a softer footprint), my mower does NOT throw clippings into mulch or flower beds, at an additional charge I offer bagging of the clippings and/or dog waste clean-up. I am thinking about a two-sided design. I would also like a cartoon style picture of myself riding my mower. If this is something you can create, I can send you a photo of myself and a photo of my mower. If not, I can get this drawing done separately, then send it to you, I would just need to know what kind of file you would need it in. I am not going to have a business name, I want to introduce myself as Dawson to keep it simple and personal. We can add a coupon to the postcard, offering one free cut with commitment to a full 26 week season. The name of my high school is Marwick High.

The cartoon picture attached is our logo.

Target Market(s)

Homeowners that use a commercial lawn cutting service, homeowners that need a temporary service while they are on vacation

Industry/Entity Type

School

Colors
3176b5
9bcb3c

Requirements
Must have
• An appeal for people to want to help me earn money for my college education. A clear idea they will be getting top notch service. I definitely want a drawing of myself on my mower. Phone # 555-271-0936
• design must work with parcelrelay.com/routeblanketmail guidelines

```html
<!DOCTYPE html>
<html lang="en">
<head>
<meta charset="utf-8">
<title>Dawson's Lawn Service – Postcard</title>
<link rel="stylesheet" href="https://fonts.googleapis.com/css2?family=Cabin:wght@500;600;700&family=Comfortaa:wght@400;600;700&family=Oswald:wght@700&display=swap">
<style>
  :root {
    --page: #e8e5df;
    --sky-blue: #3f68b0;
    --mist: #8a9a9c;
    --lawn-dark: #2f6b22;
    --lawn-mid: #4e8f2e;
    --lawn-bright: #86c232;
    --brand-green: #9bcb3c;
    --brand-blue: #3176b5;
    --cyan: #05acd4;
    --deep-red: #8e1f24;
    --star-red: #a3262b;
    --ink: #1b1b1b;
    --white: #ffffff;
  }
  * { box-sizing: border-box; margin: 0; padding: 0; }
  html, body { width: 880px; height: 1200px; overflow: hidden; background: var(--page); }
  .canvas { position: relative; width: 880px; height: 1200px; }

  .card { position: absolute; width: 722px; height: 559px; overflow: hidden; box-shadow: 0 0 0 2px #111; }

  /* ---------- Front ---------- */
  .front {
    left: 67px; top: 27px;
    background:
      linear-gradient(180deg, transparent 0 384px, rgba(134,194,50,.85) 384px, rgba(110,175,40,.9) 470px, rgba(70,135,35,.95) 559px),
      linear-gradient(200deg, var(--sky-blue) 0%, #6c86a8 22%, var(--mist) 36%, var(--lawn-mid) 55%, var(--lawn-dark) 100%);
  }
  .front .rider-art {
    position: absolute; left: 13px; top: 17px; width: 305px; height: 396px;
    border-radius: 40% 40% 20% 20%;
    background: radial-gradient(ellipse at 50% 60%, rgba(210,80,85,.55), rgba(120,110,70,.45) 55%, rgba(60,90,40,0) 75%);
  }
  .intro {
    position: absolute; left: 226px; top: 26px; width: 477px;
    font-family: "Comfortaa", sans-serif; font-size: 17.5px; line-height: 26px;
    color: var(--white); text-align: justify; text-align-last: left;
  }
  .signature {
    position: absolute; right: 27px; top: 180px;
    font-family: "Cabin", sans-serif; font-weight: 700; font-size: 20px; color: var(--ink);
  }
  .school-name {
    position: absolute; right: 20px; top: 200px;
    font-family: "Oswald", sans-serif; font-weight: 700; font-size: 68px; line-height: 90px;
    letter-spacing: 2px; color: rgba(225,225,215,.42); white-space: nowrap;
  }
  .coupon {
    position: absolute; left: 518px; top: 285px; width: 184px; height: 184px;
    border-radius: 50%; background: var(--white);
    box-shadow: 0 0 0 5px rgba(255,255,255,.85), 0 0 0 7px #9fb98a;
    text-align: center; font-family: "Cabin", sans-serif; color: var(--ink);
    padding-top: 30px;
  }
  .coupon p { line-height: 22px; }
  .coupon .small { font-size: 14px; }
  .coupon .tiny { font-size: 13px; }
  .coupon .accent { font-size: 21px; color: var(--deep-red); font-weight: 600; }
  .services-title {
    position: absolute; left: 37px; top: 403px;
    font-family: "Oswald", sans-serif; font-size: 19px; color: var(--brand-blue);
    text-decoration: underline; text-shadow: 1px 1px 0 #fff;
  }
  .services {
    position: absolute; left: 34px; top: 437px; list-style: none;
    font-family: "Cabin", sans-serif; font-weight: 500; font-size: 19px; color: var(--white);
  }
  .services li { height: 32.5px; display: flex; align-items: center; gap: 4px; white-space: nowrap; }
  .services li small { font-size: 14.5px; }
  .services svg { width: 16px; height: 16px; flex: none; }

  /* ---------- Back ---------- */
  .back { left: 108px; top: 606px; height: 558px; background: var(--white); }
  .back .color-block {
    position: absolute; left: 0; top: 0; width: 349px; height: 461px;
    background: linear-gradient(90deg, var(--brand-green) 0%, #a4cd3a 25%, #4fb9a8 55%, var(--cyan) 85%);
  }
  .back .top-strip { position: absolute; left: 0; top: 0; width: 543px; height: 178px; background: var(--cyan); }
  .back .rider-art {
    position: absolute; left: 16px; top: 18px; width: 316px; height: 440px;
    border-radius: 40% 40% 20% 20%;
    background: radial-gradient(ellipse at 50% 62%, rgba(215,80,85,.6), rgba(120,110,80,.45) 50%, rgba(40,50,90,0) 75%);
  }
  .promise {
    position: absolute; left: 228px; top: 30px; width: 310px; height: 144px;
    border: 3px solid var(--deep-red); border-radius: 6px; text-align: center;
  }
  .promise .headline {
    font-family: "Comfortaa", sans-serif; font-weight: 600; font-size: 30px; line-height: 39px;
    color: var(--deep-red); margin-top: 14px;
  }
  .promise .call {
    margin-top: 10px; font-family: "Cabin", sans-serif; font-size: 27px; font-weight: 600; color: var(--white);
  }
  .promise .call strong { color: var(--ink); margin-left: 8px; }
  .name-arc { position: absolute; left: 0; top: 0; width: 543px; height: 178px; overflow: visible; }
</style>
</head>
<body>
<main class="canvas">

  <section class="card front" aria-label="Postcard front">
    <div class="rider-art" role="img" aria-label="Cartoon illustration of Dawson in a Marwick baseball shirt riding a red commercial lawn mower"></div>
    <p class="intro">I am a high school junior, focusing on my city and the neighboring city. I am earning money for my college education. I will be working side by side with my father, who operated his own lawn service for 20 years, I will be using state of the art, commercial equipment.</p>
    <p class="signature">- DAWSON</p>
    <p class="school-name">MARWICK HIGH</p>

    <div class="coupon">
      <p class="small">Offering</p>
      <p class="small">one <span class="accent">FREE CUT</span></p>
      <p class="small">with commitment</p>
      <p class="small">to a full <span class="accent">26 WEEK</span></p>
      <p class="tiny">season</p>
    </div>

    <h2 class="services-title">My Services...</h2>
    <ul class="services">
      <li><svg viewBox="0 0 24 24"><path fill="#a3262b" d="M12 2l2.9 6.9 7.1.6-5.4 4.7 1.7 7-6.3-3.9-6.3 3.9 1.7-7L2 9.5l7.1-.6z"/></svg>My mower leaves a softer footprint <small>(light weight mower)</small></li>
      <li><svg viewBox="0 0 24 24"><path fill="#a3262b" d="M12 2l2.9 6.9 7.1.6-5.4 4.7 1.7 7-6.3-3.9-6.3 3.9 1.7-7L2 9.5l7.1-.6z"/></svg>No clippings thrown into mulch or flower beds</li>
      <li><svg viewBox="0 0 24 24"><path fill="#a3262b" d="M12 2l2.9 6.9 7.1.6-5.4 4.7 1.7 7-6.3-3.9-6.3 3.9 1.7-7L2 9.5l7.1-.6z"/></svg>Bagging of the clippings and/or dog waste clean-up <small>(at additional charge)</small></li>
    </ul>
  </section>

  <section class="card back" aria-label="Postcard back">
    <div class="color-block"></div>
    <div class="top-strip"></div>
    <div class="rider-art" role="img" aria-label="Cartoon illustration of Dawson riding his red lawn mower"></div>
    <div class="promise">
      <p class="headline">We Assured<br>Quality Results</p>
      <p class="call">CALL:<strong>555-271-0936</strong></p>
    </div>
    <svg class="name-arc" viewBox="0 0 543 178" aria-hidden="false">
      <defs><path id="arc" d="M 236 92 Q 256 32 332 30"/></defs>
      <text font-family="Comfortaa, sans-serif" font-weight="700" font-size="22" fill="#ffffff" stroke="#333333" stroke-width="1.2" paint-order="stroke" letter-spacing="1">
        <textPath href="#arc">DAWSON</textPath>
      </text>
    </svg>
  </section>

</main>
</body>
</html>
```